Business card for Full Stable Care Vandorpe

I would like to have me designed an professional business card with my existing logo for my company called : full stable care vandorpe gcv.
I prefer a two sided business card with on the back side only the horses head and the website : fscvandorpe-example.eu
Only one colour shouldbe all right.
The logo must appear in a nic professional way on the business card.

Other suggestion are welcome.

All copy wrights must be released by the designer after we have selected a final design.

Target Market(s)

Equestrian businesses

Industry/Entity Type

Business

Contact Information for Business Card

Laurent Vandorpe
Title: zaakvoerder
Full Stable Care Vandorpe GCV
Molkenweg 47
B - 2820 Bonheiden
België
Phone: + 32 491 68 27 04
Mail: laurent@fscvandorpe-example.eu

Font styles to use
Serif

Requirements
Must have
• My own logo
• See attached files
• Website: fscvandorpe-example.eu

```html
<!DOCTYPE html>
<html lang="nl">
<head>
<meta charset="utf-8">
<title>Full Stable Care Vandorpe – Business Card</title>
<link rel="stylesheet" href="https://fonts.googleapis.com/css2?family=Arimo:wght@400;700&display=swap">
<style>
  :root {
    --backdrop: #2a2a2a;
    --card-light: #ffffff;
    --card-shade: #dcdcdc;
    --ink: #111111;
    --ink-soft: #2c2c2c;
    --mark-faint: #bdbdbd;
  }
  * { box-sizing: border-box; margin: 0; padding: 0; }
  html, body {
    width: 1200px;
    height: 997px;
    overflow: hidden;
    background: var(--backdrop);
    font-family: "Arimo", Arial, sans-serif;
    color: var(--ink);
  }
  .canvas {
    position: relative;
    width: 1200px;
    height: 997px;
  }
  .card {
    position: absolute;
    left: 260px;
    width: 680px;
    height: 390px;
    border-radius: 18px;
    background: linear-gradient(160deg, var(--card-light) 0%, #f1f1f1 55%, var(--card-shade) 100%);
    overflow: hidden;
  }
  .card--back { top: 70px; }
  .card--front { top: 537px; }

  /* Back side */
  .back-mark {
    position: absolute;
    left: 160px;
    top: 36px;
    width: 200px;
    height: 200px;
    border-radius: 50%;
    background: var(--mark-faint);
    opacity: 0.55;
  }
  .back-name {
    position: absolute;
    left: 150px;
    top: 262px;
    font-weight: 700;
    font-size: 34px;
    letter-spacing: 0.5px;
    color: var(--ink);
  }

  /* Front side */
  .front-brand {
    position: absolute;
    right: 36px;
    top: 30px;
    display: flex;
    align-items: center;
    gap: 10px;
    font-weight: 700;
    font-size: 21px;
    color: var(--ink);
  }
  .front-brand__dot {
    width: 22px;
    height: 22px;
    border-radius: 50%;
    background: var(--ink);
  }
  .front-mark {
    position: absolute;
    right: 70px;
    top: 130px;
    width: 130px;
    height: 130px;
    border-radius: 50%;
    background: var(--mark-faint);
    opacity: 0.55;
  }
  .holder {
    position: absolute;
    left: 36px;
    top: 150px;
  }
  .holder__name {
    font-size: 22px;
    font-weight: 400;
    color: var(--ink-soft);
  }
  .holder__title {
    font-size: 17px;
    font-weight: 700;
    margin-top: 3px;
  }
  .rule {
    position: absolute;
    left: 236px;
    right: 40px;
    top: 190px;
    height: 2px;
    background: var(--ink);
  }
  .contact {
    position: absolute;
    left: 36px;
    top: 262px;
    list-style: none;
    font-size: 16px;
    line-height: 22px;
    color: var(--ink-soft);
  }
  .contact__item {
    display: flex;
    align-items: flex-start;
    gap: 10px;
  }
  .contact__icon {
    flex: none;
    width: 18px;
    height: 18px;
    margin-top: 2px;
  }
  .website {
    position: absolute;
    right: 40px;
    top: 290px;
    font-weight: 700;
    font-size: 15px;
    letter-spacing: 2.5px;
    color: var(--ink);
  }
</style>
</head>
<body>
<main class="canvas">

  <section class="card card--back" aria-label="Card back">
    <div class="back-mark" role="img" aria-label="Faint company emblem area"></div>
    <p class="back-name">Full Stable Care Vandorpe</p>
  </section>

  <section class="card card--front" aria-label="Card front">
    <div class="front-brand">
      <span class="front-brand__dot"></span>
      <span>Full Stable Care Vandorpe</span>
    </div>
    <div class="front-mark" role="img" aria-label="Faint company emblem area"></div>

    <div class="rule"></div>
    <div class="holder">
      <p class="holder__name">Laurent Vandorpe</p>
      <p class="holder__title">Zaakvoerder</p>
    </div>

    <ul class="contact">
      <li class="contact__item">
        <svg class="contact__icon" viewBox="0 0 18 18" aria-hidden="true">
          <circle cx="9" cy="9" r="9" fill="#111"/>
          <path d="M5.5 5h2l1 2.3-1.2.9a6 6 0 0 0 2.5 2.5l.9-1.2 2.3 1v2a1 1 0 0 1-1 1A8 8 0 0 1 4.5 6a1 1 0 0 1 1-1z" fill="#fff"/>
        </svg>
        <span>+ 32 491 68 27 04</span>
      </li>
      <li class="contact__item">
        <svg class="contact__icon" viewBox="0 0 18 18" aria-hidden="true">
          <circle cx="9" cy="9" r="9" fill="#111"/>
          <rect x="4.5" y="6" width="9" height="6.5" rx="0.8" fill="#fff"/>
          <path d="M4.8 6.4 9 9.6l4.2-3.2" fill="none" stroke="#111" stroke-width="1"/>
        </svg>
        <span>laurent@fscvandorpe-example.eu</span>
      </li>
      <li class="contact__item">
        <svg class="contact__icon" viewBox="0 0 18 18" aria-hidden="true">
          <circle cx="9" cy="9" r="9" fill="#111"/>
          <path d="M9 4.3 4 8.6h1.5v5h2.6v-3h1.8v3h2.6v-5H14z" fill="#fff"/>
        </svg>
        <span>Molkenweg 47 B-2847 Lindenhove,<br>België</span>
      </li>
    </ul>

    <p class="website">www.fscvandorpe-example.eu</p>
  </section>

</main>
</body>
</html>
```